IT Services Business Card Design

We require a business card design for an IT services company called RT Code Transit.

We specialize in taking an organisations software and readying it for deployment to new environments (e.g. Nex 3 to Nex 5). This process is termed application packaging. This is not the same as putting things in boxes but I am happy to use boxes as a pun icon ;-) This is our second step in branding, we currently have a new logo and our poor excuse of a website is next to be updated but it contains information on who we are and what we cover at rtcodetransit.example

We are looking for a fun, modern but stylish and professional looking design.

I have attached the logo in multiple formats including vector formats (and the fonts that created the logo if required)
Updates

Thanks to all the designers so far, some great designs in there.  I will be selecting a card design on the deadline date. 

However, there is still time to submit some more designs.  The majority of the ones I have so far are typical simplistic designs that we have all seen before and I have enough of those to choose from now.  If you wish to submit any more designs, please submit somthing unusual to grab our attention.

Target Market(s)

Project executives of large organisations looking for Nexora migrations

Industry/Entity Type

Software

Requirements
Must have
• Want to show company name, contact name, title, main number, contact number, fax number, email address and website address. I do not want to show the address.
Must use the attached logo, retaining the colours in them.

This has to be a double-sided design. I will be using pelby.example and will be selecting their rounded corner business card design.

Their templates and design requirements (sizing etc.) can be found here: http://uk.pelby.example/help/faq/templates-and-guidelines.html

Happy for company name or website to be on either side of the card.

This design has to be original and not used before for another company

Would like to style it around the business colours in the logo
Nice to have
• Pelby.example has an option for multiple card designs to appear on the back. If this is possible in the budget and time you have and you have a design(s) that work with that but carry the same style and theme, that would be nice to see but not necessary.
Should not have
• We do not want to put a postal address on the cards

```html
<!DOCTYPE html>
<html lang="en">
<head>
<meta charset="utf-8">
<title>RT Code Transit – Business Card</title>
<link rel="stylesheet" href="https://fonts.googleapis.com/css2?family=Questrial&display=swap">
<style>
  :root {
    --page: #f2f2f0;
    --card-dark: #282d27;
    --card-light: #ffffff;
    --ink: #5a544e;
    --ink-soft: #6e6963;
    --logo-text: #d9dcdc;
    --brand-blue: #4f72c4;
    --card-radius: 34px;
  }
  * { margin: 0; padding: 0; box-sizing: border-box; }
  html, body {
    width: 1200px; height: 1031px; overflow: hidden;
    background: var(--page);
    font-family: "Questrial", sans-serif;
  }
  .sheet {
    position: relative; width: 1200px; height: 1031px;
  }
  .card {
    position: absolute; left: 230px;
    width: 740px; height: 485px;
    border-radius: var(--card-radius);
    overflow: hidden;
    background: var(--card-dark);
    box-shadow: 0 2px 6px rgba(0,0,0,0.18);
  }
  .card--back { top: 20px; }
  .card--front { top: 526px; }

  /* back: contact side */
  .contact-panel {
    position: absolute; top: 0; right: 0;
    width: 298px; height: 100%;
    background: var(--card-light);
    border-top-right-radius: var(--card-radius);
    color: var(--ink);
  }
  .contact-name {
    position: absolute; left: 22px; top: 14px;
    font-size: 40px; letter-spacing: 0.5px; color: var(--ink);
  }
  .contact-role {
    position: absolute; left: 34px; top: 62px;
    font-size: 14px; line-height: 17px; color: var(--ink-soft);
  }
  .contact-line {
    position: absolute; left: 34px;
    display: flex; align-items: center; gap: 14px;
    font-size: 22px; color: var(--ink-soft);
  }
  .contact-line--phone { top: 162px; }
  .contact-line--fax { top: 222px; }
  .contact-line svg { width: 36px; height: 36px; }
  .social-names {
    position: absolute; right: 24px; top: 378px;
    display: flex; gap: 12px;
    font-size: 14px; color: var(--ink-soft);
  }
  .contact-web {
    position: absolute; left: 22px; top: 416px;
    font-size: 15px; color: var(--ink);
  }

  /* brand lockup */
  .brand {
    position: absolute;
    display: flex; align-items: center;
    color: var(--logo-text);
    white-space: nowrap;
  }
  .brand-dot {
    border-radius: 50%;
    background: var(--brand-blue);
    flex: none;
  }
  .brand--small { left: 34px; top: 384px; font-size: 30px; gap: 14px; }
  .brand--small .brand-dot { width: 44px; height: 44px; }
  .brand--large { left: 190px; top: 222px; font-size: 54px; gap: 22px; }
  .brand--large .brand-dot { width: 92px; height: 92px; }
</style>
</head>
<body>
<main class="sheet">

  <section class="card card--back" aria-label="Card back with contact details">
    <div class="brand brand--small">
      <span class="brand-name">RT Code Transit</span>
      <span class="brand-dot"></span>
    </div>

    <div class="contact-panel">
      <h1 class="contact-name">Sam Ardent</h1>
      <p class="contact-role">Managing Director<br>Contact No. 000 00000 00</p>

      <p class="contact-line contact-line--phone">
        <svg viewBox="0 0 36 36" aria-hidden="true">
          <path d="M9 4c2-1 4 0 5 2l2 5c1 2 0 3-1 4l-2 2c2 4 5 7 9 9l2-2c1-1 2-2 4-1l5 2c2 1 3 3 2 5l-1 2c-1 2-3 3-6 2C17 30 6 19 4 10c-1-3 0-5 2-6z" fill="var(--ink-soft)"/>
        </svg>
        <span>0000 0000 000</span>
      </p>

      <p class="contact-line contact-line--fax">
        <svg viewBox="0 0 36 36" aria-hidden="true">
          <rect x="10" y="4" width="16" height="10" fill="none" stroke="var(--ink-soft)" stroke-width="2"/>
          <rect x="3" y="14" width="30" height="16" rx="2" fill="var(--ink-soft)"/>
          <rect x="8" y="19" width="20" height="2" fill="#fff"/>
          <rect x="8" y="24" width="20" height="2" fill="#fff"/>
        </svg>
        <span>000 000 000</span>
      </p>

      <p class="social-names"><span>Flitter</span><span>Gatherly</span></p>
      <p class="contact-web">www.rtcodetransit.example</p>
    </div>
  </section>

  <section class="card card--front" aria-label="Card front with company name">
    <div class="brand brand--large">
      <span class="brand-name">RT Code Transit</span>
      <span class="brand-dot"></span>
    </div>
  </section>

</main>
</body>
</html>
```